App Re Design for professional app

Looking to have an app we have in development. We are not happy with the overall current feel and wanting a a fresh new feel. It is essentially a dating app but for professionals- where a mentor is matched with a mentee.
We need to be able to switch between a mentor interface and a mentee interface
Will have a section for searching different mentors and booking them for either a phone call, chat or video call. Here is the logo Peak4Path and the icons for the different professionals

```html
<!DOCTYPE html>
<html lang="en">
<head>
<meta charset="utf-8">
<title>Peak4Path Mentor – App Screens</title>
<link href="https://fonts.googleapis.com/css2?family=Mulish:wght@400;600;700;800;900&display=swap" rel="stylesheet">
<style>
:root{
  --stage:#151515;
  --teal-dark:#0b4d5e;
  --cyan:#2eb8d8;
  --mist:#d5edf3;
  --header:#e3f3fa;
  --card:#e2f3fa;
  --ink:#111;
  --text:#2f3b40;
  --white:#fff;
}
*{box-sizing:border-box;margin:0;padding:0}
html,body{width:1200px;height:534px;overflow:hidden;background:var(--stage);font-family:"Mulish",sans-serif}
.canvas{position:relative;width:1200px;height:534px}
.screen{position:absolute;overflow:hidden;background:var(--white)}
.screen--phone{left:64px;top:51px;width:202px;height:434px;border-radius:24px}
.screen--choose{left:325px;top:38px;width:259px;height:460px}
.screen--browse{left:605px;top:38px;width:259px;height:460px}
.screen--profile{left:892px;top:38px;width:259px;height:460px}

/* choose screen */
.hill{position:absolute;left:-25%;width:150%;bottom:-40px;background:var(--mist);border-radius:50% 50% 0 0/70px 70px 0 0}
.screen--phone .hill{top:300px}
.screen--choose .hill{top:296px}
.brand{position:absolute;left:0;right:0;text-align:center;color:var(--teal-dark);font-weight:900;letter-spacing:.3px}
.brand-dot{position:absolute;left:50%;border:4px solid var(--cyan);border-radius:50%}
.screen--phone .brand-dot{width:64px;height:64px;top:49px;margin-left:-32px}
.screen--choose .brand-dot{width:74px;height:74px;top:26px;margin-left:-37px}
.screen--phone .brand{top:118px;font-size:18px;line-height:20px}
.screen--choose .brand{top:106px;font-size:23px;line-height:25px}
.choose-title{position:absolute;left:0;right:0;text-align:center;font-weight:900;color:var(--ink);letter-spacing:.5px}
.screen--phone .choose-title{top:174px;font-size:18px}
.screen--choose .choose-title{top:168px;font-size:22px}
.role-btn{position:absolute;display:flex;align-items:center;border-radius:40px;color:var(--white);font-weight:800}
.role-btn--mentor{background:var(--cyan)}
.role-btn--mentee{background:var(--teal-dark)}
.role-btn .role-icon{fill:var(--white)}
.role-btn .chev{margin-left:auto;stroke:var(--white);fill:none;stroke-width:2.4}
.screen--phone .role-btn{left:8px;width:191px;height:37px;font-size:9.5px;padding:0 18px 0 16px;gap:12px}
.screen--phone .role-btn--mentor{top:215px}
.screen--phone .role-btn--mentee{top:264px}
.screen--phone .role-icon{width:18px;height:18px}
.screen--phone .chev{width:12px;height:14px}
.screen--choose .role-btn{left:21px;width:218px;height:42px;font-size:11px;padding:0 20px 0 18px;gap:16px}
.screen--choose .role-btn--mentor{top:215px}
.screen--choose .role-btn--mentee{top:271px}
.screen--choose .role-icon{width:22px;height:22px}
.screen--choose .chev{width:13px;height:17px}

/* app chrome */
.app-header{position:absolute;top:0;left:0;right:0;height:31px;background:var(--header);display:flex;align-items:center;padding:0 12px;gap:7px}
.app-header .back{width:8px;height:13px;stroke:var(--teal-dark);stroke-width:1.8;fill:none}
.app-header .mark{width:17px;height:17px;border:2px solid var(--cyan);border-radius:50%}
.app-header .title{font-size:7.5px;font-weight:800;color:var(--teal-dark);letter-spacing:.2px}
.app-header .tools{margin-left:auto;display:flex;gap:10px}
.app-header .tools svg{width:11px;height:11px;stroke:var(--teal-dark);fill:none;stroke-width:1.6}
.tab-bar{position:absolute;left:0;right:0;bottom:0;height:47px;background:var(--teal-dark);display:flex;justify-content:space-around;align-items:center;padding:0 6px}
.tab{display:flex;flex-direction:column;align-items:center;gap:5px;color:var(--white);font-size:6.8px;font-weight:600;width:40px}
.tab svg{width:11px;height:11px;fill:var(--white)}

/* browse screen */
.section-title{position:absolute;left:0;right:0;text-align:center;color:var(--teal-dark);font-weight:900;font-size:10px;letter-spacing:.2px}
.section-title::after{content:"";display:block;width:15px;height:1px;background:var(--teal-dark);margin:7px auto 0}
.section-title--categories{top:44px}
.section-title--mentors{top:166px}
.categories{position:absolute;top:77px;left:4px;right:4px;display:flex;justify-content:space-between}
.category{width:62px;display:flex;flex-direction:column;align-items:center;gap:5px}
.category-badge{width:46px;height:46px;border-radius:50%;border:2px solid var(--teal-dark);display:flex;align-items:center;justify-content:center;box-shadow:0 0 0 2px var(--white),0 0 0 3px var(--cyan)}
.category-badge span{font-size:15px;font-weight:900;color:var(--teal-dark);letter-spacing:-.3px}
.category-label{font-size:4.6px;font-weight:800;color:var(--teal-dark);text-transform:uppercase;letter-spacing:.2px;white-space:nowrap}
.browse-divider{position:absolute;top:150px;left:0;right:0;height:6px;background:linear-gradient(#f2f6f8,#fff)}
.mentor-grid{position:absolute;top:195px;left:7px;width:242px;display:grid;grid-template-columns:repeat(3,76px);column-gap:7px;row-gap:8px;justify-content:space-between}
.mentor-card{height:98px;background:var(--card);border-radius:10px;overflow:hidden}
.mentor-photo{height:67px;border-radius:10px}
.mentor-name{font-size:6.2px;font-weight:800;color:var(--teal-dark);margin:8px 0 0 8px}
.mentor-role{font-size:5.2px;color:var(--text);margin:2px 0 0 8px}
.tone-1{background:linear-gradient(160deg,#cfd3d4,#a9896a)}
.tone-2{background:linear-gradient(160deg,#e6e8ea,#8c2638)}
.tone-3{background:linear-gradient(160deg,#6f7376,#9d9a97)}
.tone-4{background:linear-gradient(160deg,#e9eef1,#1d2536)}
.tone-5{background:linear-gradient(160deg,#8cc3e0,#3f6d9e)}
.tone-6{background:linear-gradient(160deg,#dcdcdc,#b8cbe0)}

/* profile screen */
.hero{position:absolute;top:31px;left:0;right:0;height:104px;background:linear-gradient(100deg,#6b7a83 0%,#9eb4c4 45%,#c7d5dd 100%)}
.hero-name{position:absolute;left:12px;top:70px;color:var(--white);font-weight:900;font-size:11px;letter-spacing:.3px}
.hero-role{position:absolute;left:12px;top:85px;color:var(--white);font-size:7.5px;font-weight:600}
.contact-band{position:absolute;top:135px;left:0;right:0;height:40px;background:var(--teal-dark);display:flex;justify-content:space-between;padding:8px 11px}
.contact-btn{width:74px;height:24px;border:1px solid #9fc7d2;display:flex;align-items:center;justify-content:center;gap:6px;color:var(--white);font-size:7px;font-weight:800}
.contact-btn svg{width:10px;height:10px;fill:var(--white)}
.about{position:absolute;top:184px;left:11px;right:10px}
.about h2{font-size:10.5px;font-weight:900;color:var(--teal-dark)}
.about p{margin-top:6px;font-size:6px;line-height:9.3px;color:var(--text)}
.facts{margin-top:6px;display:flex;gap:11px;font-size:7px;font-weight:800;color:var(--teal-dark)}
.profile-divider{position:absolute;top:294px;left:0;right:0;height:5px;background:linear-gradient(#f1f5f7,#fff)}
.activities{position:absolute;top:307px;left:12px;right:8px}
.activities h3{font-size:8px;font-weight:900;color:var(--teal-dark)}
.activity-row{margin-top:6px;display:grid;grid-template-columns:repeat(3,76px);column-gap:6px}
.activity-photo{height:55px}
.activity-caption{margin-top:8px;font-size:6.4px;font-weight:800;color:var(--ink);line-height:8.5px}
.tone-a{background:linear-gradient(160deg,#d7d3cd,#8e9aa8)}
.tone-b{background:linear-gradient(160deg,#f0efec,#c9c2b8)}
.tone-c{background:linear-gradient(160deg,#a99a8c,#4e6b86)}
</style>
</head>
<body>
<svg width="0" height="0" style="position:absolute" aria-hidden="true">
  <defs>
    <symbol id="i-chev" viewBox="0 0 12 20"><path d="M2 2l8 8-8 8"/></symbol>
    <symbol id="i-back" viewBox="0 0 8 14"><path d="M7 1L1 7l6 6"/></symbol>
    <symbol id="i-search" viewBox="0 0 12 12"><circle cx="5" cy="5" r="4"/><path d="M8 8l3.3 3.3"/></symbol>
    <symbol id="i-bell" viewBox="0 0 12 12"><path d="M3 8.5V5a3 3 0 016 0v3.5l1 1H2zM5 10.5a1 1 0 002 0"/></symbol>
    <symbol id="i-people" viewBox="0 0 24 24"><circle cx="12" cy="6" r="3"/><path d="M7 14a5 5 0 0110 0z"/><circle cx="5" cy="14" r="2.4"/><circle cx="19" cy="14" r="2.4"/><path d="M1 22a4 4 0 018 0zM15 22a4 4 0 018 0z"/></symbol>
    <symbol id="i-hands" viewBox="0 0 24 24"><path d="M1 9l5-3 5 2 2-1 5 0 5 3-2 5-4 4-3-1-3 1-4-3-4-2z"/></symbol>
    <symbol id="i-home" viewBox="0 0 12 12"><path d="M6 1L0.5 6H2v5h3V8h2v3h3V6h1.5z"/></symbol>
    <symbol id="i-chat" viewBox="0 0 12 12"><path d="M1 1h10v7H5l-3 3V8H1z"/></symbol>
    <symbol id="i-phone" viewBox="0 0 12 12"><path d="M2.5 1l2 2.5-1 1.2a7 7 0 003.8 3.8l1.2-1 2.5 2-1 2C5 11.5.5 7 1 1.8z"/></symbol>
    <symbol id="i-video" viewBox="0 0 12 12"><path d="M1 3h7v6H1zM8.5 5.2L11 3.5v5L8.5 6.8z"/></symbol>
    <symbol id="i-gear" viewBox="0 0 12 12"><path d="M5 0h2l.3 1.6 1.3.6 1.4-.9 1.4 1.4-.9 1.4.6 1.3L12 5v2l-1.6.3-.6 1.3.9 1.4-1.4 1.4-1.4-.9-1.3.6L7 12H5l-.3-1.6-1.3-.6-1.4.9-1.4-1.4.9-1.4-.6-1.3L0 7V5l1.6-.3.6-1.3-.9-1.4 1.4-1.4 1.4.9 1.3-.6zM6 4a2 2 0 100 4 2 2 0 000-4z"/></symbol>
  </defs>
</svg>

<main class="canvas">

  <section class="screen screen--phone" aria-label="Choose role">
    <div class="hill"></div>
    <div class="brand-dot"></div>
    <div class="brand">Peak4Path<br>Mentor</div>
    <h1 class="choose-title">CHOOSE</h1>
    <a class="role-btn role-btn--mentor"><svg class="role-icon"><use href="#i-people"/></svg>MENTOR<svg class="chev"><use href="#i-chev"/></svg></a>
    <a class="role-btn role-btn--mentee"><svg class="role-icon"><use href="#i-hands"/></svg>MENTEE<svg class="chev"><use href="#i-chev"/></svg></a>
  </section>

  <section class="screen screen--choose" aria-label="Choose role">
    <div class="hill"></div>
    <div class="brand-dot"></div>
    <div class="brand">Peak4Path<br>Mentor</div>
    <h1 class="choose-title">CHOOSE</h1>
    <a class="role-btn role-btn--mentor"><svg class="role-icon"><use href="#i-people"/></svg>MENTOR<svg class="chev"><use href="#i-chev"/></svg></a>
    <a class="role-btn role-btn--mentee"><svg class="role-icon"><use href="#i-hands"/></svg>MENTEE<svg class="chev"><use href="#i-chev"/></svg></a>
  </section>

  <section class="screen screen--browse" aria-label="Browse mentors">
    <header class="app-header">
      <svg class="back"><use href="#i-back"/></svg><span class="mark"></span><span class="title">HEADING</span>
      <span class="tools"><svg><use href="#i-search"/></svg><svg><use href="#i-bell"/></svg></span>
    </header>
    <h2 class="section-title section-title--categories">CATEGORIES</h2>
    <div class="categories">
      <div class="category"><div class="category-badge"><span>OT</span></div><span class="category-label">Occupational Therapist</span></div>
      <div class="category"><div class="category-badge"><span>PT</span></div><span class="category-label">Physiotherapist</span></div>
      <div class="category"><div class="category-badge"><span>PSY</span></div><span class="category-label">Psychologist</span></div>
      <div class="category"><div class="category-badge"><span>SW</span></div><span class="category-label">Social Worker</span></div>
    </div>
    <div class="browse-divider"></div>
    <h2 class="section-title section-title--mentors">MENTORS</h2>
    <div class="mentor-grid">
      <article class="mentor-card"><div class="mentor-photo tone-1" role="img" aria-label="Portrait photo of mentor Ellis"></div><p class="mentor-name">Ellis</p><p class="mentor-role">Lorem Ipsum nsectetur</p></article>
      <article class="mentor-card"><div class="mentor-photo tone-2" role="img" aria-label="Portrait photo of mentor Rowan"></div><p class="mentor-name">Rowan</p><p class="mentor-role">Lorem Ipsum nsectetur</p></article>
      <article class="mentor-card"><div class="mentor-photo tone-3" role="img" aria-label="Portrait photo of mentor Tavish"></div><p class="mentor-name">Tavish</p><p class="mentor-role">Lorem Ipsum nsectetur</p></article>
      <article class="mentor-card"><div class="mentor-photo tone-4" role="img" aria-label="Portrait photo of mentor Quincy"></div><p class="mentor-name">Quincy</p><p class="mentor-role">Lorem Ipsum nsectetur</p></article>
      <article class="mentor-card"><div class="mentor-photo tone-5" role="img" aria-label="Portrait photo of mentor Hadley"></div><p class="mentor-name">Hadley</p><p class="mentor-role">Lorem Ipsum nsectetur</p></article>
      <article class="mentor-card"><div class="mentor-photo tone-6" role="img" aria-label="Portrait photo of mentor Ellis"></div><p class="mentor-name">Ellis</p><p class="mentor-role">Lorem Ipsum nsectetur</p></article>
    </div>
    <nav class="tab-bar">
      <span class="tab"><svg><use href="#i-home"/></svg>Home</span>
      <span class="tab"><svg><use href="#i-chat"/></svg>Chat</span>
      <span class="tab"><svg><use href="#i-phone"/></svg>Phone</span>
      <span class="tab"><svg><use href="#i-video"/></svg>Video</span>
      <span class="tab"><svg><use href="#i-gear"/></svg>Settings</span>
    </nav>
  </section>

  <section class="screen screen--profile" aria-label="Mentor profile">
    <header class="app-header">
      <svg class="back"><use href="#i-back"/></svg><span class="mark"></span><span class="title">HEADING</span>
      <span class="tools"><svg><use href="#i-search"/></svg><svg><use href="#i-bell"/></svg></span>
    </header>
    <div class="hero" role="img" aria-label="Photo of mentor Corbin smiling in an office">
      <p class="hero-name">CORBIN</p>
      <p class="hero-role">Manager</p>
    </div>
    <div class="contact-band">
      <a class="contact-btn"><svg><use href="#i-phone"/></svg>PHONE</a>
      <a class="contact-btn"><svg><use href="#i-video"/></svg>VIDEO</a>
      <a class="contact-btn"><svg><use href="#i-chat"/></svg>CHAT</a>
    </div>
    <div class="about">
      <h2>ABOUT</h2>
      <p>Lorem ipsum dolor sit amet, consectetur adipiscing elit, sed do eiusmod tempor incididunt ut labore et dolore magna aliqua. Ut enim ad minim veniam, quis nostrud exercitation ullamco laboris nisi ut aliquip ex ea commodo consequat. Duis aute irure dolor in repre henderit in voluptate velit esse cillum dolore eu fugiat nulla pariatur. Excepteur sint occaecat cupidatat non proident, sunt in culpa qui officia deserunt mollit anim id est labo Excepteur sint occaecat cupidatat non proident, sunt in culpa qui officia deseru.</p>
      <div class="facts"><span>Experience : 10</span><span>Qualification : B.C.A</span></div>
    </div>
    <div class="profile-divider"></div>
    <div class="activities">
      <h3>RECENT ACTIVITIES</h3>
      <div class="activity-row">
        <div><div class="activity-photo tone-a" role="img" aria-label="Photo of a group mentoring session"></div><p class="activity-caption">Lorem ipsum dolor sit amet, consectetu</p></div>
        <div><div class="activity-photo tone-b" role="img" aria-label="Photo of a one-to-one counselling session"></div><p class="activity-caption">Lorem ipsum dolor sit amet, consectetu</p></div>
        <div><div class="activity-photo tone-c" role="img" aria-label="Photo of a mentor talking with a client"></div><p class="activity-caption">Lorem ipsum dolor sit amet, consectetu</p></div>
      </div>
    </div>
    <nav class="tab-bar">
      <span class="tab"><svg><use href="#i-home"/></svg>Home</span>
      <span class="tab"><svg><use href="#i-chat"/></svg>Chat</span>
      <span class="tab"><svg><use href="#i-phone"/></svg>Phone</span>
      <span class="tab"><svg><use href="#i-video"/></svg>Video</span>
      <span class="tab"><svg><use href="#i-gear"/></svg>Settings</span>
    </nav>
  </section>

</main>
</body>
</html>
```